Eye Grabbing - Travel Consultant Business Card

I need a business card that stands out. Vertical instead of horizontal, rounded edges, would love to use the same layout item for magnets. I have uploaded my current logo and tag line. Would love a cool eye-grabbing image for the front side. Can be something different than what you see on my website as I am looking to rebrand as a Leisure, Luxury & Adventure Specialist.

Target Market(s)

Leisure and Luxury Travel

Industry/Entity Type

Travel Agent

Contact Information for Business Card

Company Name - Ombrella Voyages; Name - Priya Halworth; Title - Travel Consultant; Website - www.ombrellavoyages.com ; Phone: 318-662-0954 Email priya@ombrellavoyages.com and my facebook, twitter, and Instagram handles

Font styles to use
Serif

Colors

Designer to choose colors to be used in the design.

Requirements
Must have
• my tag line of -- Dream Explore Discover
Nice to have

```html
<!DOCTYPE html>
<html lang="en">
<head>
<meta charset="utf-8">
<title>Ombrella Voyages – Business Card</title>
<link rel="stylesheet" href="https://fonts.googleapis.com/css2?family=Merriweather:ital,wght@0,400;0,700;0,900;1,400&display=swap">
<style>
  :root {
    --royal: #2c3e9b;
    --leaf: #4caf50;
    --teal: #2fa6b0;
    --ink: #3a3a3a;
    --paper: #ffffff;
    --stage: #e6e7ea;
    --serif: "Merriweather", Georgia, serif;
  }
  * { box-sizing: border-box; margin: 0; padding: 0; }
  html, body { width: 1200px; height: 900px; overflow: hidden; }
  body {
    background: var(--stage);
    font-family: var(--serif);
    position: relative;
  }
  .card {
    position: absolute;
    top: 150px;
    width: 350px;
    height: 600px;
    border-radius: 22px;
    overflow: hidden;
    box-shadow: 0 10px 28px rgba(0,0,0,.18);
  }

  /* ---------- back side ---------- */
  .card--back {
    left: 195px;
    background: var(--royal);
    color: var(--paper);
  }
  .brand {
    position: absolute;
    left: 0; right: 0;
    text-align: center;
  }
  .card--back .brand { top: 180px; }
  .brand__dot {
    display: block;
    margin: 0 auto 18px;
    width: 74px; height: 74px;
    border-radius: 50%;
    background: var(--paper);
  }
  .brand__name {
    font-weight: 900;
    font-size: 28px;
    line-height: 1.1;
  }
  .back-tagline {
    position: absolute;
    left: 0; right: 0;
    top: 478px;
    text-align: center;
    font-style: italic;
    font-size: 17px;
  }
  .social {
    position: absolute;
    left: 0; right: 0;
    top: 516px;
    display: flex;
    justify-content: center;
    gap: 12px;
  }
  .social span {
    width: 13px; height: 13px;
    border-radius: 50%;
    background: var(--paper);
  }
  .back-rule {
    position: absolute;
    left: 0; right: 0;
    top: 556px;
    height: 1px;
    background: var(--leaf);
  }

  /* ---------- front side ---------- */
  .card--front {
    left: 655px;
    background: var(--paper);
    color: var(--ink);
  }
  .side-band {
    position: absolute;
    left: 0; top: 0; bottom: 0;
    width: 26px;
    background: var(--royal);
  }
  .side-band::before {
    content: "";
    position: absolute;
    left: 0; top: 0;
    width: 26px; height: 70px;
    background: var(--leaf);
  }
  .corner-mark {
    position: absolute;
    left: 42px; top: 24px;
    width: 30px; height: 30px;
    border-radius: 50%;
    background: var(--teal);
  }
  .card--front .brand {
    top: 70px;
    left: auto;
    right: 28px;
    text-align: right;
    color: var(--royal);
  }
  .card--front .brand__dot {
    margin: 0 0 14px auto;
    width: 80px; height: 80px;
    background: var(--teal);
  }
  .card--front .brand__name { font-size: 25px; }

  .person {
    position: absolute;
    left: 60px;
    top: 320px;
  }
  .person__name {
    font-weight: 900;
    font-size: 26px;
    color: var(--royal);
  }
  .person__title {
    margin-top: 8px;
    font-style: italic;
    font-size: 15px;
  }
  .person__rule {
    margin: 14px 0 16px;
    width: 22px; height: 2px;
    background: var(--royal);
  }
  .contact { list-style: none; }
  .contact li {
    display: flex;
    align-items: center;
    gap: 12px;
    font-style: italic;
    font-size: 14px;
    margin-bottom: 12px;
  }
  .contact svg { flex: none; width: 22px; height: 22px; }
</style>
</head>
<body>

<section class="card card--back" aria-label="Card back">
  <div class="brand">
    <span class="brand__dot"></span>
    <div class="brand__name">Ombrella Voyages</div>
  </div>
  <p class="back-tagline">Dream Explore Discover</p>
  <div class="social" aria-label="Social profiles"><span></span><span></span><span></span></div>
  <div class="back-rule"></div>
</section>

<section class="card card--front" aria-label="Card front">
  <div class="side-band"></div>
  <span class="corner-mark"></span>
  <div class="brand">
    <span class="brand__dot"></span>
    <div class="brand__name">Ombrella Voyages</div>
  </div>

  <div class="person">
    <h1 class="person__name">Priya Halworth</h1>
    <p class="person__title">Travel Consultant</p>
    <div class="person__rule"></div>
    <ul class="contact">
      <li>
        <svg viewBox="0 0 22 22" aria-hidden="true"><circle cx="11" cy="11" r="11" fill="#2c3e9b"/><path d="M8 6.5l1.6 2.6-1 1.1a6 6 0 0 0 3.2 3.2l1.1-1 2.6 1.6-.8 1.6c-3.8.3-7.9-3.8-7.6-7.6z" fill="#fff"/></svg>
        318-662-0954
      </li>
      <li>
        <svg viewBox="0 0 22 22" aria-hidden="true"><circle cx="11" cy="11" r="11" fill="#2c3e9b"/><rect x="6" y="7.5" width="10" height="7" rx="1" fill="#fff"/><path d="M6.5 8l4.5 3.5L15.5 8" fill="none" stroke="#2c3e9b" stroke-width="1"/></svg>
        priya@ombrellavoyages.com
      </li>
      <li>
        <svg viewBox="0 0 22 22" aria-hidden="true"><circle cx="11" cy="11" r="11" fill="#2c3e9b"/><circle cx="11" cy="11" r="5" fill="none" stroke="#fff" stroke-width="1.2"/><path d="M6 11h10M11 6c-2.2 2.8-2.2 7.2 0 10M11 6c2.2 2.8 2.2 7.2 0 10" fill="none" stroke="#fff" stroke-width="1"/></svg>
        www.ombrellavoyages.com
      </li>
    </ul>
  </div>
</section>

</body>
</html>
```